Structural Engineering Business Card

Veltrow Drafts does residential house plans for clients in Central Florida. Would like simple but elegant business card that is appropriate for a house plan engineering company. Prefer black business card with black/white them but open to other shades of blue. I uploaded a sample card that I came across that looked good but please come up with your own creative designs.

Contact Information for Business Card

Name, Title, Phone, Email, Address, website

```html
<!DOCTYPE html>
<html lang="en">
<head>
<meta charset="utf-8">
<title>Veltrow Drafts — Business Card</title>
<link rel="stylesheet" href="https://fonts.googleapis.com/css2?family=Montserrat:wght@400;700&display=swap">
<style>
  :root {
    --stage: #2b2b2b;
    --card-top: #3a3a36;
    --card-bottom: #24241f;
    --ink: #f2f2f0;
    --ink-soft: #d9d9d4;
    --rule: #9a9a94;
    --accent-square: #e4ede6;
    --sketch-light: #4a4a45;
    --sketch-dark: #2f2f2b;
  }
  * { box-sizing: border-box; margin: 0; padding: 0; }
  html, body {
    width: 1200px; height: 900px; overflow: hidden;
    background: var(--stage);
    font-family: "Montserrat", sans-serif;
  }
  .canvas { position: relative; width: 1200px; height: 900px; }
  .card {
    position: absolute;
    border-radius: 22px;
    background: linear-gradient(180deg, var(--card-top), var(--card-bottom));
    box-shadow: 0 18px 40px rgba(0,0,0,0.55);
    overflow: hidden;
    color: var(--ink);
  }
  .card-front { left: 80px; top: 300px; width: 540px; height: 310px; }
  .card-back  { left: 720px; top: 190px; width: 310px; height: 540px; }

  .front-skyline {
    position: absolute; left: 150px; right: 0; top: 110px; bottom: 0;
    background: linear-gradient(180deg, rgba(80,80,74,0.35), rgba(60,60,55,0.15));
    clip-path: polygon(0 60%, 10% 60%, 10% 30%, 30% 30%, 30% 10%, 50% 10%, 50% 35%, 72% 35%, 72% 0, 85% 0, 85% 25%, 100% 25%, 100% 100%, 0 100%);
  }
  .brand-name {
    position: absolute; left: 0; right: 0; top: 118px;
    text-align: center;
    font-weight: 700; font-size: 40px; letter-spacing: 2px;
    color: var(--ink);
    text-transform: uppercase;
  }

  .back-skyline {
    position: absolute; left: 0; top: 0; width: 310px; height: 250px;
    background: linear-gradient(160deg, var(--sketch-light), var(--sketch-dark));
    clip-path: polygon(35% 0, 100% 0, 100% 42%, 100% 100%, 78% 88%, 40% 78%, 10% 70%, 0 62%, 0 30%);
  }
  .back-details { position: absolute; left: 36px; top: 268px; right: 24px; }
  .person-name {
    font-weight: 700; font-size: 17px; letter-spacing: 4px; text-transform: uppercase;
  }
  .person-title {
    margin-top: 4px; font-size: 12px; letter-spacing: 1.5px; color: var(--ink-soft);
  }
  .rule { width: 46px; height: 1px; background: var(--rule); margin: 14px 0; }
  .contact-line { font-size: 12.5px; letter-spacing: 1.2px; line-height: 1.6; color: var(--ink-soft); }
  .accent-square {
    position: absolute; left: 36px; bottom: 26px; width: 20px; height: 20px;
    background: var(--accent-square);
  }
</style>
</head>
<body>
<div class="canvas">
  <section class="card card-front" aria-label="Card front">
    <div class="front-skyline" role="img" aria-label="Faint line drawing of a city skyline"></div>
    <h1 class="brand-name">Veltrow Drafts</h1>
  </section>

  <section class="card card-back" aria-label="Card back">
    <div class="back-skyline" role="img" aria-label="White line drawing of stacked city buildings"></div>
    <div class="back-details">
      <p class="person-name">Dorian Hale</p>
      <p class="person-title">Managing Director</p>
      <div class="rule"></div>
      <p class="contact-line">+00 98-765-4321</p>
      <div class="rule"></div>
      <p class="contact-line">000 N Harbor Lane<br>Ocala, FL 00000</p>
      <p class="contact-line">dorian@veltrowdrafts.com</p>
      <p class="contact-line">veltrowdrafts.com</p>
    </div>
    <div class="accent-square"></div>
  </section>
</div>
</body>
</html>
```